New Website

New website is to be the same as Copper Lantern.

Website needs to be fully functional, with only text and logo to be added by client at a later date.

Logo has been added for reference.

Reason: waiting for the final submissions to be completed.

```html
<!DOCTYPE html>
<html lang="en">
<head>
<meta charset="utf-8">
<title>Veltora — The Right Expert</title>
<link rel="stylesheet" href="https://fonts.googleapis.com/css2?family=Open+Sans:ital,wght@0,400;0,600;0,700;1,600&family=Tinos:wght@400;700&family=Roboto:wght@400&display=swap">
<style>
:root{
  --header:#0f2a30;
  --teal-dark:#0b262b;
  --accent:#3a9bd5;
  --red:#d9434b;
  --ink:#333;
  --line:#d6d6d6;
  --white:#fff;
  --footer:#0b0b0b;
  --footer-bar:#161616;
  --footer-text:#8a8a8a;
}
*{box-sizing:border-box;margin:0;padding:0}
html,body{width:1200px;height:2719px;overflow:hidden}
body{position:relative;background:var(--white);font-family:"Open Sans",sans-serif;color:var(--ink)}
.abs{position:absolute}

/* header */
.site-header{position:absolute;left:0;top:0;width:1200px;height:120px;background:var(--header)}
.brand{position:absolute;left:100px;top:32px;display:flex;align-items:center;gap:14px}
.brand-dot{width:56px;height:56px;border-radius:50%;background:#2f5f8c}
.brand-name{font-size:30px;font-weight:400;color:#4f86c6;letter-spacing:1px}
.main-nav{position:absolute;top:52px;left:478px}
.main-nav a{color:var(--white);text-decoration:none;font-size:13px;font-weight:700;position:absolute;white-space:nowrap}
.main-nav a.active{color:var(--accent)}
.main-nav a.active::after{content:"";position:absolute;left:0;right:0;bottom:-9px;height:2px;background:var(--accent)}
.btn-outline{position:absolute;top:45px;height:30px;border:1.5px solid #d8d8c0;color:var(--white);font-size:12px;font-weight:700;display:flex;align-items:center;justify-content:center}

/* hero */
.hero{position:absolute;left:0;top:120px;width:1200px;height:466px}
.hero-photo{position:absolute;inset:0;background:linear-gradient(90deg,#2b1f17 0%,#5a4330 30%,#6b5443 55%,#4b3a33 72%,#2a2a30 100%)}
.hero-portrait{position:absolute;left:730px;top:0;width:370px;height:466px;background:radial-gradient(ellipse at 50% 45%,#b8937a 0%,#6f5546 45%,#232830 100%)}
.hero-title{position:absolute;left:100px;top:84px;font-family:"Tinos",serif;font-weight:700;color:var(--white);font-size:45px;letter-spacing:1px;line-height:1}
.hero-sub{position:absolute;left:100px;top:142px;font-family:"Tinos",serif;font-weight:700;color:var(--white);font-size:31px;line-height:1}
.hero-lead{position:absolute;left:100px;top:204px;color:var(--white);font-size:16px;font-weight:600}
.hero-cta{position:absolute;left:100px;top:275px;width:344px;height:48px;background:#1d2a22;color:var(--white);font-size:15px;font-weight:700;display:flex;align-items:center;padding-left:24px;gap:12px}
.slider-dots{position:absolute;left:100px;top:362px;display:flex;gap:6px}
.slider-dots span{width:13px;height:13px;border-radius:50%;border:2px solid #9bbf3a}
.slider-dots span.on{border-color:var(--white)}
.find-tab{position:absolute;left:838px;top:1px;width:262px;height:37px;background:#2f6f86;color:var(--white);font-size:17px;font-weight:700;display:flex;align-items:center;justify-content:center;gap:10px;clip-path:polygon(20px 0,100% 0,100% 100%,0 100%)}
.video-tab{position:absolute;left:827px;top:344px;width:273px;height:38px;background:#2f6f86;color:var(--white);font-size:16px;font-weight:700;display:flex;align-items:center;justify-content:center;gap:10px;clip-path:polygon(20px 0,100% 0,100% 100%,0 100%)}
.expert-card{position:absolute;left:827px;top:382px;width:273px;height:84px;background:rgba(22,40,24,.92);color:var(--white);padding:22px 0 0 17px}
.expert-card h3{font-size:19px;font-weight:700;letter-spacing:.5px}
.expert-card p{font-size:11.5px;font-weight:600;margin-top:12px}

/* services */
.section-title{position:absolute;left:0;width:1200px;text-align:center;font-size:23px;font-weight:600;color:#333}
.service-card{position:absolute;top:723px;width:316px;height:207px;border:1px solid #cfcfcf;background:var(--white);text-align:center;padding-top:62px}
.service-card::after{content:"";position:absolute;left:20px;right:20px;bottom:-22px;height:20px;background:radial-gradient(ellipse at 50% 0,rgba(0,0,0,.28) 0%,rgba(0,0,0,0) 70%)}
.service-icon{position:absolute;left:121px;top:-36px;width:74px;height:74px;border-radius:50%;background:var(--accent);border:3px solid #e9f3fa;display:flex;align-items:center;justify-content:center}
.service-card h3{font-size:14px;font-weight:700;color:#333}
.service-card p{font-size:11.5px;line-height:20px;color:#444;margin:10px 18px 0}
.btn-red{display:inline-flex;margin-top:14px;height:26px;padding:0 13px;background:var(--red);color:var(--white);font-size:11px;align-items:center}
.divider{position:absolute;left:100px;top:983px;width:1000px;height:1px;background:var(--line)}

/* call to action */
.cta{position:absolute;left:100px;top:1028px;width:1000px;height:419px;overflow:hidden}
.cta-photo{position:absolute;inset:0;background:linear-gradient(100deg,#2a2622 0%,#4a3f37 35%,#3b3c40 65%,#2c2a29 100%)}
.cta h2{position:absolute;left:0;right:0;top:108px;text-align:center;color:var(--white);font-size:32px;font-weight:600}
.cta p{position:absolute;left:0;right:0;top:171px;text-align:center;color:var(--white);font-size:12.5px;line-height:22px}
.cta-input{position:absolute;left:195px;top:254px;width:459px;height:56px;background:rgba(150,150,150,.55);color:#e7e7e7;font-size:11px;padding-left:16px;display:flex;align-items:center}
.cta-btn{position:absolute;left:665px;top:254px;width:143px;height:56px;background:var(--accent);color:var(--white);font-size:16px;display:flex;align-items:center;justify-content:center}

/* video + news */
.media-band{position:absolute;left:0;top:1489px;width:1200px;height:413px;background:var(--teal-dark)}
.media-band::after{content:"";position:absolute;left:150px;right:150px;bottom:-34px;height:32px;background:radial-gradient(ellipse at 50% 0,rgba(0,0,0,.35) 0%,rgba(0,0,0,0) 70%)}
.band-title{position:absolute;top:58px;color:var(--white);font-size:22px;font-weight:400}
.video-thumb{position:absolute;left:100px;top:143px;width:313px;height:181px;border:2px solid #c9d4da;background:linear-gradient(135deg,#8fb3cc 0%,#d9e4ea 45%,#6f8796 100%)}
.video-bar{position:absolute;left:6px;right:6px;bottom:6px;height:14px;background:#24323a}
.play{position:absolute;left:128px;top:70px;width:54px;height:36px;background:rgba(20,20,20,.75);display:flex;align-items:center;justify-content:center}
.video-caption{position:absolute;left:100px;top:335px;width:313px;text-align:center;color:var(--white);font-size:12.5px;font-weight:600}
.news{position:absolute;top:134px;width:324px;text-align:center;color:var(--white)}
.news-sep{position:absolute;top:134px;width:1px;height:210px;background:rgba(255,255,255,.08)}
.date{position:absolute;top:0;left:126px;width:58px;height:58px;border-radius:50%;background:#2f87c6;border:3px solid #dfe8ee;display:flex;flex-direction:column;align-items:center;justify-content:center;line-height:1}
.date b{font-size:17px;font-weight:700}
.date small{font-size:9px;margin-top:3px}
.month{position:absolute;top:18px;left:196px;font-size:19px;font-weight:600}
.news h4{position:absolute;top:80px;left:0;right:0;font-size:12.5px;font-weight:700}
.news p{position:absolute;top:107px;left:0;right:0;font-size:11px;line-height:20px;color:#e3e8ea}
.news a{position:absolute;top:178px;left:0;right:0;font-size:11.5px;font-weight:700;color:var(--accent);text-decoration:none}

/* testimonials */
.avatar{position:absolute;left:542px;top:2040px;width:116px;height:116px;border-radius:50%;border:4px solid #e3e3e3;background:radial-gradient(circle at 50% 45%,#c7a48c 0%,#7c6a58 60%,#4f6b3e 100%);box-shadow:0 0 0 1px #ccc}
.quote-box{position:absolute;left:100px;top:2192px;width:1000px;height:219px;border:1px solid #d8d8d8;box-shadow:0 3px 8px rgba(0,0,0,.15);background:var(--white)}
.quote-open,.quote-close{position:absolute;font-family:"Tinos",serif;font-size:64px;color:#999;line-height:1}
.quote-text{position:absolute;left:134px;top:34px;width:800px;font-size:11px;line-height:20px;color:#555}
.quote-name{position:absolute;right:84px;top:156px;font-size:19px;color:#333;text-align:right}
.quote-role{position:absolute;right:84px;top:184px;font-size:13px;font-style:italic;font-weight:600;color:#333}
.arrow{position:absolute;top:2290px}

/* footer */
.site-footer{position:absolute;left:0;top:2453px;width:1200px;height:218px;background:var(--footer);font-family:"Roboto",sans-serif}
.footer-title{position:absolute;top:30px;color:var(--white);font-size:15px;font-weight:400}
.footer-title.serif{font-family:"Tinos",serif;font-size:18px}
.footer-about{position:absolute;left:100px;top:66px;width:260px;font-size:11px;line-height:19.5px;color:var(--footer-text);text-align:justify}
.footer-map{position:absolute;left:486px;top:58px;width:248px;height:127px;background:linear-gradient(180deg,#1c2022,#141617)}
.map-label{position:absolute;font-size:11.5px;color:#cfcfcf}
.contact-row{position:absolute;left:870px;display:flex;align-items:flex-start;gap:16px;font-size:12px;line-height:19px;color:var(--footer-text)}
.contact-ico{width:22px;height:22px;border-radius:50%;background:#2e2e2e;flex:none;display:flex;align-items:center;justify-content:center}
.footer-bar{position:absolute;left:0;top:2671px;width:1200px;height:48px;background:var(--footer-bar);font-family:"Roboto",sans-serif}
.copyright{position:absolute;left:176px;top:16px;font-size:11.5px;color:#777}
.social{position:absolute;top:12px;width:26px;height:26px;border-radius:50%;border:1.5px solid #777}
</style>
</head>
<body>

<header class="site-header">
  <div class="brand"><span class="brand-dot"></span><span class="brand-name">VELTORA</span></div>
  <nav class="main-nav">
    <a class="active" style="left:0">HOME</a>
    <a style="left:74px">HOW IT WORKS</a>
    <a style="left:203px">PRODUCTS</a>
    <a style="left:304px">BLOG</a>
    <a style="left:374px">HELP</a>
  </nav>
  <span class="btn-outline" style="left:931px;width:80px">SIGN IN</span>
  <span class="btn-outline" style="left:1021px;width:79px">RGISTER</span>
</header>

<section class="hero">
  <div class="hero-photo" role="img" aria-label="Blurred warm office interior behind the hero"></div>
  <div class="hero-portrait" role="img" aria-label="Portrait of a smiling business expert in a dark suit"></div>
  <h1 class="hero-title">THE RIGHT EXPERT</h1>
  <p class="hero-sub">RIGHT NOW</p>
  <p class="hero-lead">Lorem Ipsum is simply dummy text standard dummy text</p>
  <a class="hero-cta">BROWSE BUSINESS CATEGORIES
    <svg width="18" height="18" viewBox="0 0 18 18"><circle cx="9" cy="9" r="9" fill="#fff"/><path d="M7 5l4 4-4 4" stroke="#1d2a22" stroke-width="2" fill="none"/></svg></a>
  <div class="slider-dots"><span></span><span></span><span class="on"></span></div>
  <div class="find-tab">
    <svg width="15" height="15" viewBox="0 0 15 15"><circle cx="6" cy="6" r="4.5" stroke="#fff" stroke-width="2" fill="none"/><path d="M9.5 9.5l4 4" stroke="#fff" stroke-width="2"/></svg>
    FIND YOUR EXPERT
    <svg width="10" height="12" viewBox="0 0 10 12"><path d="M0 0l10 6-10 6z" fill="#fff"/></svg>
  </div>
  <div class="video-tab">
    <svg width="18" height="18" viewBox="0 0 18 18"><circle cx="9" cy="9" r="8" stroke="#fff" stroke-width="1.6" fill="none"/><path d="M7 5.5l5 3.5-5 3.5z" fill="#fff"/></svg>
    WATCH THE VIDEO
  </div>
  <div class="expert-card"><h3>MARCO ELLING</h3><p>EXPERTISE : HEALTH CARE CONSUMERISM</p></div>
</section>

<h2 class="section-title" style="top:624px">SERVICES</h2>

<article class="service-card" style="left:100px">
  <span class="service-icon"><svg width="30" height="30" viewBox="0 0 30 30"><path d="M4 13h5v13H4zM11 13l5-9c2 0 3 1 3 3l-1 5h7c2 0 3 2 2 4l-3 8c-1 2-2 2-3 2H11z" fill="#fff"/></svg></span>
  <h3>LOREM IPSUM IS SIMPLY DUMMY</h3>
  <p>But I must explain to you how all this mistaken idea of denouncing pleasure and praising pain was born and I will give you a complete account of the</p>
  <span class="btn-red">VIEW MORE</span>
</article>
<article class="service-card" style="left:444px">
  <span class="service-icon"><svg width="30" height="30" viewBox="0 0 30 30"><circle cx="15" cy="9" r="6" fill="#fff"/><path d="M4 28c0-7 5-11 11-11s11 4 11 11z" fill="#fff"/><path d="M15 18l-2 3 2 6 2-6z" fill="#3a9bd5"/></svg></span>
  <h3>LOREM IPSUM IS SIMPLY DUMMY</h3>
  <p>But I must explain to you how all this mistaken idea of denouncing pleasure and praising pain was born and I will give you a complete account of the</p>
  <span class="btn-red">VIEW MORE</span>
</article>
<article class="service-card" style="left:785px">
  <span class="service-icon"><svg width="32" height="32" viewBox="0 0 32 32"><circle cx="12" cy="13" r="7" fill="none" stroke="#fff" stroke-width="4" stroke-dasharray="3 2.5"/><circle cx="12" cy="13" r="2.5" fill="#fff"/><circle cx="23" cy="23" r="4.5" fill="none" stroke="#fff" stroke-width="3" stroke-dasharray="2 2"/></svg></span>
  <h3>LOREM IPSUM IS SIMPLY DUMMY</h3>
  <p>But I must explain to you how all this mistaken idea of denouncing pleasure and praising pain was born and I will give you a complete account of the</p>
  <span class="btn-red">VIEW MORE</span>
</article>

<div class="divider"></div>

<section class="cta">
  <div class="cta-photo" role="img" aria-label="Business people talking in a meeting, darkened behind the text"></div>
  <h2>ACCUSAMUS ET IUSTO ODIO DUCIMUS QUI BLANDITIIS !!</h2>
  <p>Must explain to you how all this mistaken idea of denouncing pleasure and praising pain was born and I will give you a complete account of<br>The system, and expound the actual teachings of the great explorer of the truth, the master-builder of human happiness</p>
  <div class="cta-input">ENTER YOUR EMAIL ADDRESS</div>
  <div class="cta-btn">CLICK JOIN US</div>
</section>

<section class="media-band">
  <h2 class="band-title" style="left:200px">OUR VIDEO</h2>
  <h2 class="band-title" style="left:703px">LATEST NEWS</h2>
  <div class="video-thumb" role="img" aria-label="Video still of colleagues at an office table">
    <span class="play"><svg width="16" height="18" viewBox="0 0 16 18"><path d="M0 0l16 9-16 9z" fill="#fff"/></svg></span>
    <div class="video-bar"></div>
  </div>
  <p class="video-caption">VERO EOS ET ACCUSAMUS ET IUSTO ODIO</p>
  <span class="news-sep" style="left:436px"></span>
  <span class="news-sep" style="left:784px"></span>
  <article class="news" style="left:444px">
    <div class="date"><b>12</b><small>2015</small></div><span class="month">JAN</span>
    <h4>LOREM IPSUM DOLOR SIT</h4>
    <p>Amet, consectetuer adipiscing elit, sed dia nonummy nibh euismod tincidunt laoreet dolore magna aliquam massa laoreet. erat volutpat. Ut veniamquis</p>
    <a>MORE +</a>
  </article>
  <article class="news" style="left:786px">
    <div class="date"><b>20</b><small>2015</small></div><span class="month">JAN</span>
    <h4>LOREM IPSUM DOLOR SIT</h4>
    <p>Amet, consectetuer adipiscing elit, sed dia nonummy nibh euismod tincidunt laoreet dolore magna aliquam massa laoreet. erat volutpat. Ut veniamquis</p>
    <a>MORE +</a>
  </article>
</section>

<h2 class="section-title" style="top:1975px">TESTOMONIALS</h2>
<div class="avatar" role="img" aria-label="Portrait photo of the client giving the testimonial"></div>
<section class="quote-box">
  <span class="quote-open" style="left:82px;top:22px">&ldquo;</span>
  <p class="quote-text">There are many variations of passages of Lorem Ipsum available, but the majority have suffered alteration in some form, by injected humour, or rdomised words which don't look even slightly believable. If you are going to use a passage of Lorem Ipsum, you need to be sure there isn't anything embarrassing hidden in the middle of text. All the Lorem Ipsum generators on the generate Lorem Ipsum</p>
  <span class="quote-close" style="left:620px;top:100px">&rdquo;</span>
  <p class="quote-name">DANA CORVELL</p>
  <p class="quote-role">—CEO, Brightfield Co</p>
</section>
<svg class="arrow" style="left:110px" width="12" height="20" viewBox="0 0 12 20"><path d="M10 2L2 10l8 8" stroke="#333" stroke-width="2.2" fill="none"/></svg>
<svg class="arrow" style="left:1078px" width="12" height="20" viewBox="0 0 12 20"><path d="M2 2l8 8-8 8" stroke="#333" stroke-width="2.2" fill="none"/></svg>

<footer class="site-footer">
  <h3 class="footer-title serif" style="left:100px">About VELTORA</h3>
  <p class="footer-about">Risus mollis malesuada quis quis nulla. Vestibulum ante ipsum primis in faucibus orci luctus et ultrices posuere cubilia mattis vel elit porttitor euismod pharetra sem interdum.<br>Etiam laoreet sagittis placerat magna sit amet massa posuere pretiumulum id est nulla, non</p>

  <h3 class="footer-title" style="left:490px">Our Locations</h3>
  <div class="footer-map" role="img" aria-label="Dark world map marking the office locations"></div>
  <span class="map-label" style="left:599px;top:74px">Lorem Dummy</span>
  <span class="map-label" style="left:599px;top:120px">Lorem Dummy</span>

  <h3 class="footer-title" style="left:870px">Get In Touch</h3>
  <div class="contact-row" style="top:63px"><span class="contact-ico"><svg width="10" height="13" viewBox="0 0 10 13"><path d="M5 13S0 7 0 5a5 5 0 0110 0c0 2-5 8-5 8z" fill="#888"/></svg></span><span style="width:200px;text-align:justify">Lorem Ipsum is simply dummy text of the printing</span></div>
  <div class="contact-row" style="top:117px"><span class="contact-ico"><svg width="12" height="10" viewBox="0 0 12 10"><path d="M1 2c2-2 8-2 10 0v2H8V3H4v1H1zM2 5h8l1 5H1z" fill="#888"/></svg></span><span>Toll free:&nbsp; +000 111 888</span></div>
  <div class="contact-row" style="top:157px"><span class="contact-ico"><svg width="12" height="9" viewBox="0 0 12 9"><rect x=".5" y=".5" width="11" height="8" fill="none" stroke="#888"/><path d="M.5.5l5.5 4 5.5-4" fill="none" stroke="#888"/></svg></span><span>info@veltora.example</span></div>
</footer>

<div class="footer-bar">
  <p class="copyright">Copyright © 2014. veltora.example. All rights reserved</p>
  <span class="social" style="left:933px"></span>
  <span class="social" style="left:965px"></span>
  <span class="social" style="left:997px"></span>
</div>

</body>
</html>
```